Stonegate Towing Business Card

Towing
Accident towing
Mechanical breakdown
Insurance, salvage and recovery
4wd off road towing
Light & Heavy towing
7354 2618
24 hour business 7 days

Logo can be whole size on front

Industry/Entity Type

Towing/ transport

Contact Information for Business Card

The above

```html
<!DOCTYPE html>
<html lang="en">
<head>
<meta charset="utf-8">
<title>Stonegate Towing Business Card</title>
<link rel="stylesheet" href="https://fonts.googleapis.com/css2?family=Figtree:wght@400;500&family=Montserrat:wght@700;800&display=swap">
<style>
  :root {
    --backdrop: #b1b1b1;
    --brand-red: #d32128;
    --ink: #111111;
    --paper: #ffffff;
  }
  * { margin: 0; padding: 0; box-sizing: border-box; }
  html, body {
    width: 1200px; height: 716px; overflow: hidden;
    background: var(--backdrop);
    font-family: "Montserrat", sans-serif;
  }
  .canvas { position: relative; width: 1200px; height: 716px; }
  .card {
    position: absolute; left: 370px; width: 460px; height: 264px; overflow: hidden;
  }
  .card--front { top: 94px; background: var(--brand-red); }
  .card--back { top: 385px; background: var(--paper); }

  .wordmark {
    position: absolute; left: 0; right: 0; text-align: center;
    font-weight: 800; line-height: 1; white-space: nowrap;
  }
  .card--front .wordmark {
    top: 108px; font-size: 40px; color: var(--paper); letter-spacing: 0.5px;
  }
  .card--back .wordmark {
    top: 44px; font-size: 24px; color: var(--brand-red);
  }

  .services {
    position: absolute; top: 111px; left: 0; right: 0;
    font-family: "Figtree", sans-serif;
    font-size: 12.5px; font-weight: 500; color: var(--ink); line-height: 15px;
  }
  .service-row {
    display: flex; justify-content: center; gap: 11px;
    list-style: none; height: 19.5px;
  }
  .service-row li { display: flex; align-items: center; gap: 6px; white-space: nowrap; }
  .tick { width: 12px; height: 12px; flex: none; }

  .phone {
    position: absolute; top: 176px; left: 0; right: 0;
    display: flex; justify-content: center; align-items: center; gap: 8px;
    font-size: 33px; font-weight: 700; color: var(--ink); line-height: 1;
  }
  .phone-icon { width: 34px; height: 28px; }
  .hours {
    position: absolute; top: 213px; left: 0; right: 0; text-align: center;
    font-size: 11px; font-weight: 800; letter-spacing: 3.2px; color: var(--ink);
    white-space: nowrap;
  }
  .footer-band { position: absolute; left: 0; bottom: 0; width: 460px; height: 28px; }
</style>
</head>
<body>
<main class="canvas">
  <section class="card card--front" aria-label="Card front">
    <div class="wordmark">Stonegate Towing</div>
  </section>

  <section class="card card--back" aria-label="Card back">
    <div class="wordmark">Stonegate Towing</div>

    <div class="services">
      <ul class="service-row">
        <li><svg class="tick" viewBox="0 0 12 12"><circle cx="6" cy="6" r="6" fill="var(--brand-red)"/><path d="M3.3 6.2l1.8 1.8 3.6-3.8" fill="none" stroke="#fff" stroke-width="1.5"/></svg>Towing</li>
        <li><svg class="tick" viewBox="0 0 12 12"><circle cx="6" cy="6" r="6" fill="var(--brand-red)"/><path d="M3.3 6.2l1.8 1.8 3.6-3.8" fill="none" stroke="#fff" stroke-width="1.5"/></svg>Accident Towing</li>
        <li><svg class="tick" viewBox="0 0 12 12"><circle cx="6" cy="6" r="6" fill="var(--brand-red)"/><path d="M3.3 6.2l1.8 1.8 3.6-3.8" fill="none" stroke="#fff" stroke-width="1.5"/></svg>Mechanical Breakdown</li>
      </ul>
      <ul class="service-row">
        <li><svg class="tick" viewBox="0 0 12 12"><circle cx="6" cy="6" r="6" fill="var(--brand-red)"/><path d="M3.3 6.2l1.8 1.8 3.6-3.8" fill="none" stroke="#fff" stroke-width="1.5"/></svg>Insurance, Salvage and Recovery</li>
        <li><svg class="tick" viewBox="0 0 12 12"><circle cx="6" cy="6" r="6" fill="var(--brand-red)"/><path d="M3.3 6.2l1.8 1.8 3.6-3.8" fill="none" stroke="#fff" stroke-width="1.5"/></svg>4wd off Road Towing</li>
      </ul>
      <ul class="service-row">
        <li><svg class="tick" viewBox="0 0 12 12"><circle cx="6" cy="6" r="6" fill="var(--brand-red)"/><path d="M3.3 6.2l1.8 1.8 3.6-3.8" fill="none" stroke="#fff" stroke-width="1.5"/></svg>Light &amp; Heavy towing</li>
      </ul>
    </div>

    <div class="phone">
      <svg class="phone-icon" viewBox="0 0 34 28" aria-hidden="true">
        <path d="M2 9c0-5 6-7 15-7s15 2 15 7v2h-7V8c-2-1-5-1-8-1s-6 0-8 1v3H2z" fill="var(--brand-red)"/>
        <path d="M9 10h16l5 16H4z" fill="var(--brand-red)"/>
        <g fill="#fff"><rect x="13" y="14" width="2" height="2"/><rect x="16" y="14" width="2" height="2"/><rect x="19" y="14" width="2" height="2"/><rect x="13" y="17" width="2" height="2"/><rect x="16" y="17" width="2" height="2"/><rect x="19" y="17" width="2" height="2"/><rect x="13" y="20" width="2" height="2"/><rect x="16" y="20" width="2" height="2"/><rect x="19" y="20" width="2" height="2"/></g>
      </svg>
      <span>7354 2618</span>
    </div>
    <p class="hours">24 Hour Business 7 Days</p>

    <svg class="footer-band" viewBox="0 0 460 28" aria-hidden="true">
      <rect x="0" y="15" width="460" height="13" fill="var(--ink)"/>
      <path d="M105 28 Q125 0 150 0 H310 Q335 0 357 28 Z" fill="var(--paper)"/>
      <path d="M110 28 Q129 3 152 3 H308 Q331 3 352 28 Z" fill="var(--brand-red)"/>
    </svg>
  </section>
</main>
</body>
</html>
```